Clara Joy Halden- Lantern Waltz- Autumn/Winter Tour Dates

I need high res A3 Tour poster for print and for social media JPG sharing of tour dates.
Also needed Facebook/Twitter Banner Cover Photos of these dates.
Text Needed Below
Clara Joy Halden
Lantern Waltz
Autumn/Winter Tour Dates
03/09 Ravensby Folk Festival
21/09 Swindon- Calder Theatre
01/10 Hitchin- Brackwell Folk Club
17/10 Bath- The Anvil
20/10 Sheffield- Upper Dale Croquet Club
24/10 Birmingham- Orchard Lamp Cafe
26/10 Glasgow- The Nook and Jar
27/10 Edinburgh - The Marble Parlour
08/11 Capital Reel and Ballad Festival- The Crooked Heron
25/11 Lewes- Tandem Record Shop- Live In Store
02/12 Cambridge- The Quayside
27/01 Lincolnshire- Fenmarsh Theatre
Tickets/Info: www.clarajoyhalden-music.example/gigs
(Quotes/Reviews To Put On)
"Outstanding, rich and expressive."            "Vibrant and Experimental"
**** BdM                                                               **** Tunepaths
"Impressive and Invigorating"                        "Enchanting" Acoustic Wire UK
tBarks

Updates
I cannot read the tour dates on most of the submissions so far. They need to be visible to viewers.
Thank You.
Please also be as creative and inventive as possible- not bland.

Target Market(s)
Music Fans- Folk Acoustic Americana
Industry/Entity Type
Media
Font styles to use
Requirements
Must have
- My photo featured prominently
- Look classy and not tacky or OTT
- Look elegant, wintery and eye catching
- The dates must be very clear to read
- Links to Website:

Nice to have
- Something innovative and not boring in terms of layout design
- Perhaps fading/ misty or wintery

Should not have
- Any colours that do not match

```html
<!DOCTYPE html>
<html lang="en">
<head>
<meta charset="utf-8">
<title>Clara Joy Halden – Lantern Waltz Tour Poster</title>
<link rel="stylesheet" href="https://fonts.googleapis.com/css2?family=Libre+Caslon+Display&family=Libre+Caslon+Text:wght@400;700&family=Source+Sans+3:ital,wght@0,400;0,700;0,900;1,400&display=swap">
<style>
  :root {
    --canvas: #e4e4e4;
    --night: #0d0722;
    --gold: #f5c542;
    --lemon: #f4f53c;
    --magenta: #e23fe6;
    --ink: #ffffff;
    --muted: #b9b3cc;
    --rule: rgba(255,255,255,0.55);
    --band-top: #1a0b38;
    --band-bottom: #241048;
  }
  html, body {
    margin: 0;
    width: 1135px;
    height: 1200px;
    overflow: hidden;
    background: var(--canvas);
  }
  .poster {
    position: absolute;
    left: 171px;
    top: 40px;
    width: 792px;
    height: 1120px;
    overflow: hidden;
    background: var(--night);
    font-family: "Source Sans 3", sans-serif;
    color: var(--ink);
  }
  .backdrop {
    position: absolute;
    inset: 0 0 164px 0;
    background:
      radial-gradient(ellipse 260px 330px at 660px 200px, rgba(214,228,222,0.95), rgba(120,150,170,0.45) 55%, transparent 100%),
      radial-gradient(ellipse 420px 380px at 90px 360px, rgba(150,60,170,0.75), transparent 75%),
      linear-gradient(180deg, #1c0d3e 0%, #3b1866 40%, #2a1458 70%, #0e0828 100%);
  }
  .portrait {
    position: absolute;
    left: 330px;
    top: 100px;
    width: 462px;
    height: 856px;
    background:
      radial-gradient(ellipse 110px 150px at 210px 290px, rgba(226,200,205,0.55), transparent 80%),
      radial-gradient(ellipse 230px 420px at 230px 440px, rgba(25,18,45,0.85), transparent 85%);
  }
  .date-panel {
    position: absolute;
    left: 0;
    top: 430px;
    width: 560px;
    height: 526px;
  }
  .artist-name {
    position: absolute;
    top: 14px;
    left: 0;
    width: 100%;
    margin: 0;
    text-align: center;
    font-family: "Libre Caslon Display", serif;
    font-weight: 400;
    font-size: 96px;
    line-height: 1.2;
    white-space: nowrap;
    color: var(--ink);
  }
  .tour-title {
    position: absolute;
    left: 40px;
    top: 136px;
    margin: 0;
    font-family: "Libre Caslon Display", serif;
    font-weight: 400;
    font-size: 86px;
    line-height: 84px;
    color: var(--lemon);
  }
  .tour-title span { display: block; }
  .tour-heading {
    position: absolute;
    left: 38px;
    top: 466px;
    margin: 0;
    color: var(--magenta);
    font-weight: 900;
    line-height: 1;
  }
  .tour-heading .season { display: block; font-size: 29px; font-weight: 700; letter-spacing: 0.3px; }
  .tour-heading .label { display: block; font-size: 41px; margin-top: 2px; }
  .date-list {
    position: absolute;
    left: 41px;
    top: 551px;
    margin: 0;
    padding: 0;
    list-style: none;
    font-size: 18.5px;
    line-height: 29.6px;
  }
  .date-list li {
    display: flex;
    width: max-content;
    border-bottom: 1px solid var(--rule);
    height: 28.6px;
  }
  .date-list li.no-rule { border-bottom: none; }
  .date-list li.cont { padding-left: 60px; }
  .date { width: 60px; color: var(--gold); font-weight: 700; }
  .town { font-weight: 700; }
  .tickets {
    position: absolute;
    left: 0;
    bottom: 0;
    width: 100%;
    height: 164px;
    background: linear-gradient(180deg, var(--band-top), var(--band-bottom) 60%, #1a0a36);
    text-align: center;
  }
  .tickets-line {
    margin: 26px 0 0;
    font-family: "Libre Caslon Text", serif;
    font-weight: 700;
    font-size: 27px;
    white-space: nowrap;
  }
  .tickets-line .url { color: var(--gold); }
  .reviews { margin: 12px 0 0; font-size: 17.5px; line-height: 28px; }
  .source { color: var(--muted); font-style: italic; margin-left: 10px; }
</style>
</head>
<body>
<main class="poster">
  <div class="backdrop" role="img" aria-label="Misty violet winter sky with falling snow"></div>
  <div class="portrait" role="img" aria-label="Portrait of the singer wearing a crystal crown among falling snowflakes"></div>
  <svg class="date-panel" viewBox="0 0 560 526" aria-hidden="true">
    <polygon points="0,0 290,0 520,380 440,526 0,526" fill="#0c0620" opacity="0.55"/>
  </svg>

  <h1 class="artist-name">Clara Joy Halden</h1>
  <h2 class="tour-title"><span>Lantern</span><span>Waltz</span></h2>

  <h3 class="tour-heading"><span class="season">AUTUMN/WINTER</span><span class="label">TOUR DATES</span></h3>

  <ul class="date-list">
    <li><span class="date">03/09</span><span>Ravensby Folk Festival</span></li>
    <li><span class="date">21/09</span><span><span class="town">Swindon</span>- Calder Theatre</span></li>
    <li><span class="date">01/10</span><span><span class="town">Hitchin</span>- Brackwell Folk Club</span></li>
    <li><span class="date">17/10</span><span><span class="town">Bath</span>- The Anvil</span></li>
    <li><span class="date">20/10</span><span><span class="town">Sheffield</span>- Upper Dale Croquet Club</span></li>
    <li><span class="date">24/10</span><span><span class="town">Birmingham</span>- Orchard Lamp Cafe</span></li>
    <li><span class="date">26/10</span><span><span class="town">Glasgow</span>- The Nook and Jar</span></li>
    <li><span class="date">27/10</span><span><span class="town">Edinburgh</span> - The Marble Parlour</span></li>
    <li class="no-rule"><span class="date">08/11</span><span class="town">Capital Reel and Ballad Festival-</span></li>
    <li class="cont"><span>The Crooked Heron</span></li>
    <li><span class="date">25/11</span><span><span class="town">Lewes</span>- Tandem Record Shop- Live In Store</span></li>
    <li><span class="date">02/12</span><span><span class="town">Cambridge</span>- The Quayside</span></li>
    <li class="no-rule"><span class="date">27/01</span><span><span class="town">Lincolnshire</span>- Fenmarsh Theatre</span></li>
  </ul>

  <footer class="tickets">
    <p class="tickets-line">Tickets/Info: <span class="url">www.clarajoyhalden-music.example/gigs</span></p>
    <p class="reviews">
      "Outstanding, rich and expressive." "Vibrant and Experimental" <span class="source">**** BdM **** Tunepaths</span><br>
      "Impressive and Invigorating" "Enchanting" <span class="source">Acoustic Wire UK tBarks</span>
    </p>
  </footer>
</main>
</body>
</html>
```